Design some Business Cards For Automotive and Instrial Film COmpany

Creating Namecard for my company
Company Name : Glazora
Customer Name : Marcus Lim
Position : Sales Manager
Phone : +6027814390
Email Address : Marcus@glazora-example.com
Address : No. 47 Lorong Cempaka Jln Seroja 11750 Bayan Lepas Pulau Pinang

Prefered Color : Blue , White
Needs to look Professional and Large

```html
<!DOCTYPE html>
<html lang="en">
<head>
<meta charset="utf-8">
<title>Glazora Business Cards</title>
<link href="https://fonts.googleapis.com/css2?family=Roboto:wght@400;500;700&display=swap" rel="stylesheet">
<style>
  :root {
    --bg: #d9d9d9;
    --card: #ffffff;
    --blue: #1f5fbf;
    --blue-deep: #1349a8;
    --orange: #f07a22;
    --text-light: #ffffff;
    --ink: #2b2b2b;
  }
  * { margin: 0; padding: 0; box-sizing: border-box; }
  html, body { width: 1200px; height: 900px; overflow: hidden; }
  body {
    background: var(--bg);
    font-family: "Roboto", Arial, sans-serif;
    position: relative;
  }
  .card {
    position: absolute;
    left: 250px;
    width: 700px;
    height: 400px;
    background: var(--card);
    border-radius: 28px;
    overflow: hidden;
    box-shadow: 0 6px 18px rgba(0,0,0,0.18);
  }
  .card-front { top: 40px; }
  .card-back { top: 460px; }

  .brand { display: flex; align-items: center; gap: 18px; position: absolute; }
  .brand-dot { border-radius: 50%; border: 5px solid var(--orange); }
  .brand-name { color: var(--blue); font-weight: 500; line-height: 1; }
  .brand-tagline {
    display: block; color: var(--ink); font-weight: 400;
    border-top: 1.5px solid var(--ink); margin-top: 6px; padding-top: 2px;
    text-align: right;
  }

  .card-front .brand { left: 130px; top: 138px; }
  .card-front .brand-dot { width: 96px; height: 96px; }
  .card-front .brand-name { font-size: 74px; }
  .card-front .brand-tagline { font-size: 15px; }

  .card-back .back-shape { position: absolute; inset: 0; width: 100%; height: 100%; }
  .card-back .brand { left: 48px; top: 150px; }
  .card-back .brand-dot { width: 62px; height: 62px; border-width: 4px; }
  .card-back .brand-name { font-size: 48px; }
  .card-back .brand-tagline { font-size: 10px; }

  .contact { position: absolute; left: 400px; top: 52px; color: var(--text-light); }
  .contact-name { color: var(--orange); font-size: 30px; font-weight: 700; }
  .contact-role { font-size: 15px; margin-top: 2px; }
  .contact-address { font-size: 15px; line-height: 1.35; margin-top: 20px; }
  .contact-list { list-style: none; margin-top: 18px; }
  .contact-list li { display: flex; align-items: center; gap: 10px; font-size: 15px; margin-bottom: 9px; }
  .contact-icon { width: 26px; height: 26px; flex: none; }
</style>
</head>
<body>

<section class="card card-front">
  <div class="brand">
    <span class="brand-dot"></span>
    <div>
      <span class="brand-name">Glazora</span>
      <span class="brand-tagline">Automotive &amp; Industrial Films</span>
    </div>
  </div>
</section>

<section class="card card-back">
  <svg class="back-shape" viewBox="0 0 700 400" preserveAspectRatio="none" aria-hidden="true">
    <defs>
      <linearGradient id="blueFill" x1="0" y1="0" x2="1" y2="1">
        <stop offset="0" stop-color="#2a6fd0"/>
        <stop offset="1" stop-color="#1245a3"/>
      </linearGradient>
    </defs>
    <path d="M280 0 C 350 40, 410 160, 400 400 L 700 400 L 700 0 Z" fill="#f07a22"/>
    <path d="M300 0 C 375 45, 432 170, 425 400 L 700 400 L 700 0 Z" fill="url(#blueFill)"/>
  </svg>

  <div class="brand">
    <span class="brand-dot"></span>
    <div>
      <span class="brand-name">Glazora</span>
      <span class="brand-tagline">Automotive &amp; Industrial Films</span>
    </div>
  </div>

  <div class="contact">
    <h1 class="contact-name">Marcus Lim</h1>
    <p class="contact-role">Sales Manager</p>
    <p class="contact-address">No. 47 Lorong Cempaka<br>Jln Seroja 11750 Bayan<br>Lepas Pulau Pinang</p>
    <ul class="contact-list">
      <li>
        <svg class="contact-icon" viewBox="0 0 26 26" aria-hidden="true">
          <circle cx="13" cy="13" r="13" fill="#f07a22"/>
          <path d="M9 7 l3 0 l1 4 l-2 1 c1 2 2 3 4 4 l1 -2 l4 1 l0 3 c-7 0 -11 -4 -11 -11z" fill="#fff"/>
        </svg>
        +6027814390
      </li>
      <li>
        <svg class="contact-icon" viewBox="0 0 26 26" aria-hidden="true">
          <circle cx="13" cy="13" r="13" fill="#f07a22"/>
          <rect x="7" y="9" width="12" height="8" fill="#fff"/>
          <path d="M7 9 l6 5 l6 -5" fill="none" stroke="#f07a22" stroke-width="1.4"/>
        </svg>
        Marcus@glazora-example.com
      </li>
      <li>
        <svg class="contact-icon" viewBox="0 0 26 26" aria-hidden="true">
          <circle cx="13" cy="13" r="13" fill="#f07a22"/>
          <circle cx="13" cy="13" r="6" fill="none" stroke="#fff" stroke-width="1.6"/>
          <path d="M7 13 h12 M13 7 c-3 3 -3 9 0 12 M13 7 c3 3 3 9 0 12" fill="none" stroke="#fff" stroke-width="1.2"/>
        </svg>
        www.glazora-example.com
      </li>
    </ul>
  </div>
</section>

</body>
</html>
```